Design some Business Cards for BWP

100% Guaranteed contest, check my history, perfect 5 star rating, I *always* select a winner and pay, even if we end up not using the winning design!!

Standard US size business cards, full color front and back.

Business cards for a company named : BWP (Brightmoor Wellness Partners)

The logo is attached, use similar color scheme.

Use following test information for the cards :

Perry Walsh
Owner
412 Elm Rd
Burleson, TX 76028
877-403-6190
info@[login to view URL]

NOTES:

1) If we see something we like we will close the project early so get your work in quick!
2) Before selecting the winner, we sort by date to ensure you have not stolen your concept from someone else (no cheating!).
3) Final hand off design to be in adobe illustrator format - no exceptions!
4) I cannot present your design to a client if it has your watermark on it. If you place a water mark your design, it will not be presented or win.

Good luck!

```html
<!DOCTYPE html>
<html lang="en">
<head>
<meta charset="utf-8">
<title>BWP Business Cards</title>
<link href="https://fonts.googleapis.com/css2?family=Cinzel:wght@500&family=PT+Sans:wght@400&display=swap" rel="stylesheet">
<style>
  :root {
    --backdrop: #d9dbde;
    --card-light: #ffffff;
    --card-shade: #e4e6e9;
    --brand-blue: #3aa6d6;
    --brand-blue-deep: #1f86b8;
    --brand-navy: #1f2a6b;
    --text-grey: #6a6f78;
  }
  * { box-sizing: border-box; margin: 0; padding: 0; }
  html, body { width: 1200px; height: 900px; overflow: hidden; }
  body {
    background: var(--backdrop);
    font-family: "PT Sans", sans-serif;
    position: relative;
  }
  .card {
    position: absolute;
    left: 260px;
    width: 680px;
    height: 388px;
    background: linear-gradient(135deg, var(--card-light) 0%, var(--card-light) 45%, var(--card-shade) 100%);
    box-shadow: 0 6px 18px rgba(0,0,0,0.25);
    overflow: hidden;
  }
  .card--back { top: 50px; }
  .card--front { top: 462px; }
  .web-band {
    position: absolute;
    top: 0; right: 0;
    width: 105px; height: 100%;
    background: linear-gradient(90deg, var(--brand-blue-deep), var(--brand-blue));
    border-left: 4px solid var(--brand-navy);
  }
  .web-band__url {
    position: absolute;
    top: 50%; left: 50%;
    transform: translate(-50%, -50%) rotate(90deg);
    color: #ffffff;
    font-size: 15px;
    letter-spacing: 3px;
    white-space: nowrap;
  }
  .brand {
    position: absolute;
    display: flex;
    align-items: center;
    color: var(--brand-navy);
  }
  .brand__dot {
    border-radius: 50%;
    background: var(--brand-blue);
    flex: none;
  }
  .brand__text { display: flex; flex-direction: column; }
  .brand__name {
    font-family: "Cinzel", serif;
    font-weight: 500;
    line-height: 1;
  }
  .brand__tagline {
    font-family: "Cinzel", serif;
    font-weight: 500;
    text-transform: uppercase;
    letter-spacing: 0.5px;
    white-space: nowrap;
  }
  .card--back .brand { left: 60px; top: 120px; gap: 18px; }
  .card--back .brand__dot { width: 116px; height: 116px; }
  .card--back .brand__name { font-size: 100px; }
  .card--back .brand__tagline { font-size: 12px; margin-top: 4px; }
  .card--front .brand { left: 36px; top: 46px; gap: 14px; }
  .card--front .brand__dot { width: 70px; height: 70px; }
  .card--front .brand__name { font-size: 56px; }
  .card--front .brand__tagline { font-size: 9px; margin-top: 2px; }
  .contact-name {
    position: absolute;
    left: 36px; top: 238px;
    font-size: 22px;
    color: var(--brand-navy);
    text-transform: uppercase;
    letter-spacing: 0.5px;
    white-space: nowrap;
  }
  .contact-name__role { color: var(--brand-blue); }
  .contact-name__divider { margin: 0 6px; }
  .contact-line {
    position: absolute;
    font-size: 12px;
    color: var(--text-grey);
    white-space: nowrap;
  }
  .contact-line__label {
    font-size: 18px;
    color: var(--brand-navy);
    margin-right: 4px;
  }
  .contact-line--phone { left: 284px; top: 240px; }
  .contact-line--email { left: 400px; top: 240px; }
  .contact-line--address { left: 36px; top: 296px; }
</style>
</head>
<body>
  <section class="card card--back" aria-label="Business card back">
    <div class="brand">
      <span class="brand__dot"></span>
      <div class="brand__text">
        <span class="brand__name">BWP</span>
        <span class="brand__tagline">Brightmoor Wellness Partners Services</span>
      </div>
    </div>
    <div class="web-band"><span class="web-band__url">www.brightmoorwp.com</span></div>
  </section>

  <section class="card card--front" aria-label="Business card front">
    <div class="brand">
      <span class="brand__dot"></span>
      <div class="brand__text">
        <span class="brand__name">BWP</span>
        <span class="brand__tagline">Brightmoor Wellness Partners Services</span>
      </div>
    </div>
    <p class="contact-name">Perry Walsh<span class="contact-name__divider">|</span><span class="contact-name__role">Owner</span></p>
    <p class="contact-line contact-line--phone"><span class="contact-line__label">P:</span>877-403-6190</p>
    <p class="contact-line contact-line--email"><span class="contact-line__label">E:</span>info@brightmoorwp.com</p>
    <p class="contact-line contact-line--address"><span class="contact-line__label">A:</span>412 Elm Rd Burleson, TX 76028</p>
    <div class="web-band"><span class="web-band__url">www.brightmoorwp.com</span></div>
  </section>
</body>
</html>
```